Varubo - Nutritious Snacks and Desserts

We need a creative e-commerce website in which all features--buttons, background, etc.--convey our message: We sell delicious, nutritious snacks and desserts that most closely comply with the paleo diet guidelines. Our first product is Grenamo®--raw, vegan, paleo chocolate balls that are made of dates, coconut, and cocoa. Our products are organic, raw, irresistible and nutritious. We have several versions of Grenamo® in development, as well as mousse, ice cream, and crackers. Our mission is to purvey basic healthy foods. Our motto is, "Fuel for the Daily Trail-Seeker(tm)."

Target Market(s)

Health-conscious professionals who tend to shop at health food stores. Our products also meet the requirements of a gluten-free diet; and they also don't contain refined sugar, so shoppers with gluten and possibly sugar issues are incidental customers.

Industry/Entity Type

Health Product

Coding

Coded - Design and coding required

Number of Pages Required

5+ page

Colors

Designer to choose colors to be used in the design.

Requirements
Must have
• We need at least a home page, a products page, an about-us page, a contact page, and a shopping cart page. We would like to be able to add products on our own later. We should be able to handle some basic coding, especially if it's just a matter of copying and modifying product pages. We would also like the ability in the future to add blogging pages, allowing us to write articles about health food and healthy lifestyle, thus attracting web-traffic (SEO).
• Other features we would like to have:
• Product photo slider on the hopepage
• Back-to-top button at the bottom of the home page
• Make sure the site is mobile-compatible
• A search bar at the top of the homepage
• "Create an account" and "Previous orders"--allowing customers to see their previous orders and reorder what they purchased in the past.
Nice to have
• We would like to convey the paleo theme without actually stating it anywhere. We'll add text as necessary, according to the page layout; you can use ipsum lorem for purpose of demonstration.

```html
<!DOCTYPE html>
<html lang="en">
<head>
<meta charset="utf-8">
<title>Varubo – Nutritious Snacks and Desserts</title>
<link href="https://fonts.googleapis.com/css2?family=Montserrat:wght@400;500;600;700&family=Open+Sans:wght@400;600&display=swap" rel="stylesheet">
<style>
:root{
  --green:#7cc142;
  --green-dark:#5fa52b;
  --green-light:#c8e6a6;
  --ink:#333333;
  --muted:#777777;
  --line:#e3e3e3;
  --panel:#f3f5f8;
  --white:#ffffff;
  --wood:#3d3028;
  --wood-deep:#2e241e;
  --hero-a:#3a2418;
}
*{box-sizing:border-box;margin:0;padding:0}
html,body{width:1200px;height:2490px;overflow:hidden}
body{position:relative;background:var(--white);font-family:"Open Sans",Arial,sans-serif;color:var(--ink)}
.abs{position:absolute}
.brand{font-family:"Montserrat",Arial,sans-serif;font-weight:600;color:var(--green);display:flex;align-items:center;gap:12px;letter-spacing:3px}
.brand-dot{border-radius:50%;background:var(--green)}

/* header */
.site-header{left:0;top:0;width:1200px;height:126px;background:var(--white);border-top:4px solid var(--green)}
.site-header .brand{left:83px;top:36px;font-size:38px}
.site-header .brand-dot{width:40px;height:40px}
.call-tab{left:838px;top:0;width:274px;height:46px;background:var(--green);color:var(--white);font-family:"Montserrat",sans-serif;font-weight:600;font-size:14px;display:flex;align-items:center;justify-content:center;gap:8px;clip-path:polygon(0 0,100% 0,92% 100%,8% 100%);letter-spacing:.5px}
.main-nav{left:0;top:84px;width:1000px;height:20px;font-family:"Montserrat",sans-serif;font-size:13px;font-weight:500;text-transform:uppercase}
.main-nav a{position:absolute;top:0;color:var(--ink);text-decoration:none;white-space:nowrap}
.main-nav a.active{color:var(--green)}
.nav-btn{top:68px;width:48px;height:48px;border:2px solid var(--green);border-radius:50%;display:flex;align-items:center;justify-content:center}

/* hero */
.hero{left:0;top:126px;width:1200px;height:518px;background:radial-gradient(ellipse at 50% 50%,#4a2f22 0%,var(--hero-a) 60%,#2a180f 100%)}
.hero-fill{position:absolute;inset:0;background:linear-gradient(90deg,rgba(150,40,30,.55) 0%,transparent 22%,transparent 78%,rgba(160,70,30,.55) 100%),linear-gradient(180deg,rgba(190,140,60,.35) 0%,transparent 30%)}
.hero .brand{position:absolute;left:0;right:0;top:118px;flex-direction:column;gap:18px;font-size:72px}
.hero .brand-dot{width:110px;height:110px;border:8px solid var(--green);background:transparent}
.hero-tag{position:absolute;left:0;right:0;top:346px;text-align:center;color:var(--white);font-family:"Montserrat",sans-serif;font-weight:600;font-size:23px;letter-spacing:.5px}
.btn{background:var(--green);color:var(--white);font-family:"Montserrat",sans-serif;font-weight:500;font-size:15px;display:flex;align-items:center;justify-content:center;border-radius:3px;text-transform:uppercase}
.hero .btn{position:absolute;left:529px;top:400px;width:142px;height:42px}
.dots{position:absolute;left:567px;top:484px;display:flex;gap:8px}
.dots span{width:16px;height:16px;border-radius:50%;border:2px solid var(--white)}
.dots span.on{border-color:var(--green)}

/* welcome */
.welcome{left:0;top:644px;width:1200px;height:214px;background:var(--green);color:var(--white);text-align:center}
.welcome h1{margin-top:35px;font-family:"Montserrat",sans-serif;font-weight:600;font-size:24px}
.welcome .rule{width:84px;height:3px;background:var(--white);margin:18px auto 26px}
.welcome p{width:580px;margin:0 auto;font-size:11.5px;line-height:26px}

/* features */
.features{left:0;top:858px;width:1200px;height:375px}
.feature{position:absolute;top:50px;width:290px;text-align:center}
.feature .ring{width:150px;height:150px;margin:0 auto;border-radius:50%;border:3px solid var(--green-light);border-top-color:var(--green);border-right-color:var(--green);display:flex;align-items:center;justify-content:center}
.feature h3{margin-top:24px;font-family:"Montserrat",sans-serif;font-weight:600;font-size:17px;color:var(--green);letter-spacing:.5px}
.feature p{margin-top:12px;font-size:11.5px;line-height:26px;color:var(--muted)}
.arrow{position:absolute;top:130px}

/* featured products */
.featured{left:0;top:1233px;width:1200px;height:473px;background:var(--panel);border-top:2px solid var(--green)}
.featured-tab{position:absolute;left:448px;top:-2px;width:330px;height:50px;background:var(--green);color:var(--white);font-family:"Montserrat",sans-serif;font-weight:500;font-size:20px;display:flex;align-items:center;justify-content:center;border-radius:0 0 40px 40px;letter-spacing:.5px}
.card{position:absolute;top:92px;width:243px;height:335px;background:var(--white);border:1px solid var(--line);text-align:center}
.card .thumb{margin:14px auto 0;width:213px;height:172px;border:1px solid #edf0f3}
.card .price{margin-top:20px;font-family:"Montserrat",sans-serif;font-weight:500;font-size:22px;color:var(--green)}
.card .name{margin-top:10px;font-family:"Montserrat",sans-serif;font-size:14px;text-transform:uppercase;letter-spacing:.5px}
.card .actions{margin-top:20px;display:flex;justify-content:center;gap:9px}
.card .actions span{width:32px;height:32px;border:1px solid #bbb;border-radius:50%;display:flex;align-items:center;justify-content:center}

/* promo */
.promo{left:0;top:1706px;width:1200px;height:478px}
.promo h2{position:absolute;left:85px;top:77px;font-family:"Montserrat",sans-serif;font-weight:600;font-size:21px;color:var(--green)}
.promo p{position:absolute;left:85px;width:545px;font-size:11.5px;line-height:25px;color:var(--muted)}
.promo .btn{position:absolute;left:85px;top:364px;width:127px;height:44px}
.promo-visual{position:absolute;left:705px;top:61px;width:350px;height:350px;border-radius:50%;background:radial-gradient(circle at 50% 45%,#b89574 0%,#8d6a4b 70%,#6e5039 100%)}

/* footer */
.site-footer{left:0;top:2184px;width:1200px;height:306px;background:linear-gradient(180deg,var(--wood) 0%,var(--wood-deep) 100%);color:var(--white)}
.site-footer .brand{position:absolute;left:116px;top:30px;flex-direction:column;gap:14px;font-size:50px}
.site-footer .brand-dot{width:106px;height:106px}
.footer-col{position:absolute;top:48px}
.footer-col h4{font-family:"Montserrat",sans-serif;font-weight:600;font-size:17px;margin-bottom:22px;letter-spacing:.3px}
.contact-list li{list-style:none;display:flex;align-items:flex-start;gap:12px;font-size:12px;line-height:16px;margin-bottom:12px}
.footer-col p{font-size:12px;line-height:19px}
.email-field{margin-top:14px;width:208px;height:34px;background:var(--white);color:#666;font-size:11px;display:flex;align-items:center;padding-left:14px}
.subscribe{margin-top:9px;width:80px;height:26px;font-size:10px;background:var(--green);color:var(--white);display:flex;align-items:center;justify-content:center;text-transform:uppercase}
.social{display:flex;gap:7px;margin-top:16px}
.social span{width:36px;height:36px;border:2px solid var(--white);border-radius:50%}
.copyright{position:absolute;left:0;right:0;top:264px;text-align:center;font-size:11px}
</style>
</head>
<body>

<header class="site-header abs">
  <div class="brand abs"><span class="brand-dot"></span>varubo</div>
  <div class="call-tab abs">
    <svg width="13" height="13" viewBox="0 0 24 24"><path fill="#fff" d="M6.6 10.8a15 15 0 0 0 6.6 6.6l2.2-2.2c.3-.3.7-.4 1-.2 1.1.4 2.3.6 3.6.6.6 0 1 .4 1 1V20c0 .6-.4 1-1 1A17 17 0 0 1 3 4c0-.6.4-1 1-1h3.5c.6 0 1 .4 1 1 0 1.3.2 2.5.6 3.6.1.3 0 .7-.2 1z"/></svg>
    <span>|&nbsp; CALL US : (000)-121-1231</span>
  </div>
  <nav class="main-nav abs">
    <a class="active" style="left:357px">Home</a>
    <a style="left:453px">About Us</a>
    <a style="left:574px">Products</a>
    <a style="left:703px">News</a>
    <a style="left:797px">Gallery</a>
    <a style="left:912px">Contact Us</a>
  </nav>
  <div class="nav-btn abs" style="left:1011px">
    <svg width="18" height="18" viewBox="0 0 24 24"><path fill="#5fa52b" d="M3 3h3l2.4 11h10.2L21 6H7.2" stroke="#5fa52b" stroke-width="1.5"/><circle cx="9" cy="19" r="1.8" fill="#5fa52b"/><circle cx="17" cy="19" r="1.8" fill="#5fa52b"/></svg>
  </div>
  <div class="nav-btn abs" style="left:1065px">
    <svg width="18" height="18" viewBox="0 0 24 24"><circle cx="10" cy="10" r="6" fill="none" stroke="#5fa52b" stroke-width="3"/><path d="M15 15l5 5" stroke="#5fa52b" stroke-width="3" stroke-linecap="round"/></svg>
  </div>
</header>

<section class="hero abs" role="img" aria-label="Dried fruits, dates and nut balls arranged on a dark wooden table">
  <div class="hero-fill"></div>
  <div class="brand"><span class="brand-dot"></span>varubo</div>
  <div class="hero-tag">FUEL FOR THE DAILY TRAIL-SEEKER ™</div>
  <div class="btn">Read More</div>
  <div class="dots"><span></span><span class="on"></span><span></span></div>
</section>

<section class="welcome abs">
  <h1>WELCOME TO VARUBO FOODS</h1>
  <div class="rule"></div>
  <p>Our products are raw, organic, vegan, gluten-free, dairy-free, fiber-rich, nutrient-dense, antioxidant-rich real foods with no preservatives, no added sugar, and no artificial or plant-based sweeteners. And they are irresistibly scrumptious!</p>
</section>

<section class="features abs">
  <svg class="arrow" style="left:38px" width="24" height="120" viewBox="0 0 24 120"><path d="M22 2L2 60l20 58" fill="none" stroke="#dcdcdc" stroke-width="2"/></svg>
  <svg class="arrow" style="left:1138px" width="24" height="120" viewBox="0 0 24 120"><path d="M2 2l20 58L2 118" fill="none" stroke="#dcdcdc" stroke-width="2"/></svg>

  <div class="feature" style="left:112px">
    <div class="ring"><svg width="84" height="70" viewBox="0 0 84 70"><circle cx="30" cy="42" r="24" fill="#7cc142"/><circle cx="60" cy="36" r="20" fill="#7cc142" stroke="#fff" stroke-width="3"/><path d="M24 18l6 4 6-4M54 14l6 4 6-4" stroke="#5fa52b" stroke-width="3" fill="none"/></svg></div>
    <h3>ORGANIC</h3>
    <p>Sed ut perspiciatis unde omnis iste natus error sit voluptatem accusantium doloremque laudantium, beatae vitae dicta sunt explicabo.</p>
  </div>
  <div class="feature" style="left:456px">
    <div class="ring"><svg width="80" height="80" viewBox="0 0 80 80"><rect x="10" y="16" width="26" height="52" rx="6" fill="none" stroke="#7cc142" stroke-width="4"/><rect x="16" y="6" width="14" height="10" fill="none" stroke="#7cc142" stroke-width="4"/><path d="M30 68V44l40-14v38z" fill="#fff" stroke="#7cc142" stroke-width="4" stroke-linejoin="round"/><path d="M30 44h40" stroke="#7cc142" stroke-width="3"/></svg></div>
    <h3>DAIRY-FREE</h3>
    <p>Sed ut perspiciatis unde omnis iste natus error sit voluptatem accusantium doloremque laudantium, beatae vitae dicta sunt explicabo.</p>
  </div>
  <div class="feature" style="left:799px">
    <div class="ring"><svg width="80" height="80" viewBox="0 0 80 80"><path d="M14 70L64 16" stroke="#7cc142" stroke-width="4" stroke-linecap="round"/><g fill="#7cc142"><ellipse cx="40" cy="36" rx="5" ry="10" transform="rotate(-45 40 36)"/><ellipse cx="50" cy="26" rx="5" ry="10" transform="rotate(-45 50 26)"/><ellipse cx="30" cy="46" rx="5" ry="10" transform="rotate(-45 30 46)"/><ellipse cx="48" cy="46" rx="5" ry="10" transform="rotate(45 48 46)"/><ellipse cx="58" cy="36" rx="5" ry="10" transform="rotate(45 58 36)"/><ellipse cx="38" cy="56" rx="5" ry="10" transform="rotate(45 38 56)"/></g></svg></div>
    <h3>GLUTEN-FREE</h3>
    <p>Sed ut perspiciatis unde omnis iste natus error sit voluptatem accusantium doloremque laudantium, beatae vitae dicta sunt explicabo.</p>
  </div>
</section>

<section class="featured abs">
  <div class="featured-tab">FEATURED PRODUCTS</div>

  <div class="card" style="left:86px">
    <div class="thumb" role="img" aria-label="Dark chocolate bar pieces" style="background:linear-gradient(135deg,#fafafa 20%,#6b3a25 45%,#3e1f12 65%,#fafafa 85%)"></div>
    <div class="price">$ 59.00</div><div class="name">Chocolate</div>
    <div class="actions"><span><svg width="14" height="14" viewBox="0 0 24 24"><path d="M3 4h3l2 10h10l2-7H7" fill="none" stroke="#999" stroke-width="2"/></svg></span><span><svg width="14" height="14" viewBox="0 0 24 24"><path d="M12 21l-8-8a5 5 0 0 1 8-6 5 5 0 0 1 8 6z" fill="none" stroke="#999" stroke-width="2"/></svg></span><span><svg width="14" height="14" viewBox="0 0 24 24"><path d="M4 8h14l-3-3M20 16H6l3 3" fill="none" stroke="#999" stroke-width="2"/></svg></span></div>
  </div>
  <div class="card" style="left:349px">
    <div class="thumb" role="img" aria-label="Swirl of chocolate mousse" style="background:radial-gradient(ellipse at 50% 55%,#a9735c 0%,#c49683 32%,#fafafa 60%)"></div>
    <div class="price">$ 59.00</div><div class="name">Mousse</div>
    <div class="actions"><span><svg width="14" height="14" viewBox="0 0 24 24"><path d="M3 4h3l2 10h10l2-7H7" fill="none" stroke="#999" stroke-width="2"/></svg></span><span><svg width="14" height="14" viewBox="0 0 24 24"><path d="M12 21l-8-8a5 5 0 0 1 8-6 5 5 0 0 1 8 6z" fill="none" stroke="#999" stroke-width="2"/></svg></span><span><svg width="14" height="14" viewBox="0 0 24 24"><path d="M4 8h14l-3-3M20 16H6l3 3" fill="none" stroke="#999" stroke-width="2"/></svg></span></div>
  </div>
  <div class="card" style="left:611px">
    <div class="thumb" role="img" aria-label="Ice cream sundae in a glass" style="background:radial-gradient(ellipse at 50% 45%,#5a3324 0%,#d9c9b8 25%,#fafafa 45%)"></div>
    <div class="price">$ 59.00</div><div class="name">Ice Cream</div>
    <div class="actions"><span><svg width="14" height="14" viewBox="0 0 24 24"><path d="M3 4h3l2 10h10l2-7H7" fill="none" stroke="#999" stroke-width="2"/></svg></span><span><svg width="14" height="14" viewBox="0 0 24 24"><path d="M12 21l-8-8a5 5 0 0 1 8-6 5 5 0 0 1 8 6z" fill="none" stroke="#999" stroke-width="2"/></svg></span><span><svg width="14" height="14" viewBox="0 0 24 24"><path d="M4 8h14l-3-3M20 16H6l3 3" fill="none" stroke="#999" stroke-width="2"/></svg></span></div>
  </div>
  <div class="card" style="left:873px">
    <div class="thumb" role="img" aria-label="Stack of golden crackers" style="background:radial-gradient(ellipse at 50% 50%,#e2a95a 0%,#efc27f 40%,#fafafa 65%)"></div>
    <div class="price">$ 59.00</div><div class="name">Crackers</div>
    <div class="actions"><span><svg width="14" height="14" viewBox="0 0 24 24"><path d="M3 4h3l2 10h10l2-7H7" fill="none" stroke="#999" stroke-width="2"/></svg></span><span><svg width="14" height="14" viewBox="0 0 24 24"><path d="M12 21l-8-8a5 5 0 0 1 8-6 5 5 0 0 1 8 6z" fill="none" stroke="#999" stroke-width="2"/></svg></span><span><svg width="14" height="14" viewBox="0 0 24 24"><path d="M4 8h14l-3-3M20 16H6l3 3" fill="none" stroke="#999" stroke-width="2"/></svg></span></div>
  </div>
</section>

<section class="promo abs">
  <h2>SELL NUTRITIOUS SNACKS</h2>
  <p style="top:128px">Sed ut perspiciatis unde omnis iste natus error sit voluptatem accusantium doloremque laudantium, totam rem aperiam, eaque ipsa quae ab illo inventore veritatis et quasi architecto beatae vitae dicta sunt explicabo. Nemo enim ipsam voluptatem quia voluptas sit aspernatur aut odit aut fugit, sed quia consequuntur magni dolores eos qui ratione voluptatem sequi nesciunt.</p>
  <p style="top:252px">Sed ut perspiciatis unde omnis iste natus error sit voluptatem accusantium doloremque laudantium, totam rem aperiam, eaque ipsa quae ab illo inventore veritatis et quasi architecto beatae vitae dicta sunt explicabo. Nemo enim ipsam voluptatem quia voluptas sit aspernatur</p>
  <div class="btn">Read More</div>
  <div class="promo-visual" role="img" aria-label="Round Grenamo product lid label with a chocolate ball, showing organic, gluten-free and vegan claims"></div>
</section>

<footer class="site-footer abs">
  <div class="brand"><span class="brand-dot"></span>varubo</div>

  <div class="footer-col" style="left:403px">
    <h4>CONTACT US</h4>
    <ul class="contact-list">
      <li><svg width="14" height="14" viewBox="0 0 24 24"><path fill="#fff" d="M6.6 10.8a15 15 0 0 0 6.6 6.6l2.2-2.2c.3-.3.7-.4 1-.2 1.1.4 2.3.6 3.6.6.6 0 1 .4 1 1V20c0 .6-.4 1-1 1A17 17 0 0 1 3 4c0-.6.4-1 1-1h3.5c.6 0 1 .4 1 1 0 1.3.2 2.5.6 3.6.1.3 0 .7-.2 1z"/></svg>(000)-121-1231 &nbsp;(Phone)</li>
      <li><svg width="14" height="14" viewBox="0 0 24 24"><rect x="6" y="3" width="12" height="6" fill="#fff"/><rect x="3" y="9" width="18" height="9" rx="2" fill="#fff"/><rect x="7" y="15" width="10" height="6" fill="#fff" stroke="#3d3028"/></svg>(000)-121-1231 &nbsp;&nbsp;&nbsp;(Fax)</li>
      <li><svg width="14" height="14" viewBox="0 0 24 24"><rect x="2" y="5" width="20" height="14" fill="none" stroke="#fff" stroke-width="2"/><path d="M2 5l10 8 10-8" fill="none" stroke="#fff" stroke-width="2"/></svg><span style="text-decoration:underline">info@varubo.com</span></li>
      <li><svg width="14" height="14" viewBox="0 0 24 24"><path fill="#fff" d="M12 2a7 7 0 0 0-7 7c0 5 7 13 7 13s7-8 7-13a7 7 0 0 0-7-7zm0 9.5a2.5 2.5 0 1 1 0-5 2.5 2.5 0 0 1 0 5z"/></svg><span># 2564 Lorem Ipsum Dummy<br>Lorem Ipsum Dummy</span></li>
    </ul>
  </div>

  <div class="footer-col" style="left:636px">
    <h4>NEWSLETTER</h4>
    <p>Register Your email address to get<br>information ablout us</p>
    <div class="email-field">Email Address</div>
    <div class="subscribe">Subscribe</div>
  </div>

  <div class="footer-col" style="left:901px">
    <h4>FOLLOW US</h4>
    <p>Lorem ipsum dolor sit amet, conse<br>ctetur adipiscing elit. Nulla in purus<br>nibh. Donec ornare</p>
    <div class="social"><span></span><span></span><span></span><span></span><span></span></div>
  </div>

  <div class="copyright">© Copyright 2018 Varubo.All Rights Reserved</div>
</footer>

</body>
</html>
```